Kovalen Spinal Care and Performance

We need new business cards, something more modern, clean. On the back of the card maybe a quote. The Dr. likes, “The doctor of the future will give no medicine, but will interest his patient in the care of the human frame, in diet and in the cause and prevention of disease.” - Walter Brisby. We are open to other suggestions. We are a chiropractic office.

```html
<!DOCTYPE html>
<html lang="en">
<head>
<meta charset="utf-8">
<title>Kovalen Spinal Care and Performance – Business Card</title>
<link rel="stylesheet" href="https://fonts.googleapis.com/css2?family=Lato:ital,wght@0,400;0,700;0,900;1,400&display=swap">
<style>
  :root {
    --stage: #2b2b2d;
    --card-white: #ffffff;
    --plum: #5a2a63;
    --plum-deep: #4a1f55;
    --olive: #3f4a1c;
    --lime: #d7dc4e;
    --rule: #b9b8aa;
    --quote-text: #e2e35a;
    --quote-credit: #f1f1f1;
  }
  * { box-sizing: border-box; margin: 0; padding: 0; }
  html, body { width: 1200px; height: 878px; overflow: hidden; }
  body {
    background: var(--stage);
    font-family: "Lato", sans-serif;
    position: relative;
  }
  .card {
    position: absolute;
    top: 284px;
    width: 540px;
    height: 309px;
    box-shadow: 0 14px 30px rgba(0,0,0,.45);
  }
  /* Front */
  .card--front { left: 36px; background: var(--card-white); }
  .holder { position: absolute; left: 34px; top: 38px; }
  .holder__name {
    font-weight: 900; font-size: 21px; letter-spacing: .3px;
    color: var(--plum-deep); text-transform: uppercase;
  }
  .holder__role {
    font-style: italic; font-size: 14px; color: var(--olive); margin-top: 1px;
  }
  .practice {
    position: absolute; right: 40px; top: 118px; width: 270px;
    display: flex; align-items: center; gap: 12px;
  }
  .practice__dot {
    flex: none; width: 14px; height: 14px; border-radius: 50%; background: var(--lime);
  }
  .practice__name {
    font-weight: 700; font-size: 22px; line-height: 1.15; color: var(--plum);
  }
  .contacts {
    position: absolute; left: 34px; top: 200px; list-style: none;
  }
  .contacts li {
    display: flex; align-items: center; gap: 10px;
    font-size: 14px; color: var(--olive); height: 20px;
  }
  .contacts svg { width: 13px; height: 13px; fill: var(--plum); flex: none; }
  .divider {
    position: absolute; left: 34px; right: 34px; top: 268px;
    border-top: 1px solid var(--rule);
  }
  .address {
    position: absolute; left: 34px; top: 276px;
    display: flex; align-items: center; gap: 10px;
    font-size: 14px; color: var(--olive);
  }
  .address svg { width: 12px; height: 14px; fill: var(--plum); }
  /* Back */
  .card--back {
    left: 624px; background: var(--plum);
    display: flex; flex-direction: column; justify-content: center;
    padding: 0 46px;
  }
  .quote {
    font-size: 16px; line-height: 1.35; color: var(--quote-text);
  }
  .quote__credit {
    margin-top: 6px; text-align: right;
    font-size: 15px; color: var(--quote-credit);
  }
</style>
</head>
<body>

<section class="card card--front" aria-label="Business card front">
  <div class="holder">
    <p class="holder__name">John Smith</p>
    <p class="holder__role">Founder &amp; CEO</p>
  </div>

  <div class="practice">
    <span class="practice__dot"></span>
    <p class="practice__name">Kovalen Spinal Care &amp; Performance</p>
  </div>

  <ul class="contacts">
    <li>
      <svg viewBox="0 0 24 24" aria-hidden="true"><path d="M6.6 10.8a15.1 15.1 0 0 0 6.6 6.6l2.2-2.2a1 1 0 0 1 1-.25 11.4 11.4 0 0 0 3.6.57 1 1 0 0 1 1 1V20a1 1 0 0 1-1 1A17 17 0 0 1 3 4a1 1 0 0 1 1-1h3.5a1 1 0 0 1 1 1c0 1.25.2 2.45.57 3.57a1 1 0 0 1-.25 1z"/></svg>
      1234567890
    </li>
    <li>
      <svg viewBox="0 0 24 24" aria-hidden="true"><path d="M2 5h20v14H2zm2 2v.4l8 5.1 8-5.1V7zm0 2.8V17h16V9.8l-8 5.1z"/></svg>
      info@yourmail.com
    </li>
    <li>
      <svg viewBox="0 0 24 24" aria-hidden="true"><path d="M12 2a10 10 0 1 0 0 20 10 10 0 0 0 0-20zm0 2c.9 1.2 1.6 2.6 2 4h-4c.4-1.4 1.1-2.8 2-4zM4.3 14a8 8 0 0 1 0-4h3.4a16 16 0 0 0 0 4zm.8 2h3c.3 1.3.8 2.5 1.5 3.6A8 8 0 0 1 5.1 16zm3-8h-3a8 8 0 0 1 4.5-3.6C8.9 5.5 8.4 6.7 8.1 8zM12 20c-.9-1.2-1.6-2.6-2-4h4c-.4 1.4-1.1 2.8-2 4zm2.3-6H9.7a14 14 0 0 1 0-4h4.6a14 14 0 0 1 0 4zm.1 5.6c.7-1.1 1.2-2.3 1.5-3.6h3a8 8 0 0 1-4.5 3.6zm1.9-5.6a16 16 0 0 0 0-4h3.4a8 8 0 0 1 0 4z"/></svg>
      www.yourwebsite.com
    </li>
  </ul>

  <div class="divider"></div>

  <p class="address">
    <svg viewBox="0 0 24 28" aria-hidden="true"><path d="M12 0a10 10 0 0 0-10 10c0 7.5 10 18 10 18s10-10.5 10-18A10 10 0 0 0 12 0zm0 14a4 4 0 1 1 0-8 4 4 0 0 1 0 8z"/></svg>
    1234 First Line Address 5678 Second Line Address
  </p>
</section>

<section class="card card--back" aria-label="Business card back">
  <blockquote class="quote">
    “The doctor of the future will give no medicine, but will interest his patient in the care of the human frame, in diet and in the cause and prevention of disease.”
  </blockquote>
  <p class="quote__credit">- Walter Brisby.</p>
</section>

</body>
</html>
```